Webdesign für Blog zum Thema WUNSCHNEST
Zielgruppe
Hallo, ich bin 41 Jahre alt und lebe mit meinem Mann und unseren beiden Kindern (und Hund Ki;)) in einem kleinen Ort im Rhein-Main-Gebiet.
Ich musste auf meine beiden Kinder jeweils lange warten und diese schwere Zeit habe ich nicht vergessen. Meine beste Freundin hat mich irgendwann dazu überredet, anderen Frauen, denen es ähnlich geht, zu helfen. Besonders kann ich mich daran erinnern, wie schwer es war, verlässliche, gut recherchierte Quellen zum Thema Wunschnest zu finden.
Zusammen mit meiner besten Freundin baue ich daher einen Blog auf, bei dem es genau um diese Themen gehen soll.
Zielgruppe:
• Frauen
• Mitte / Ende 30
• Verheiratet, keine Kinder
• Höheres Bildungsniveau / nicht zwingend Akademiker
Kernemotionen:
o grübelt / ist unsicher
o nimmt ungewollte Kinderlosigkeit persönlich
o ängstlich / teils verzweifelt
o ungeduldig
Aufgabenstellung
Es geht um das Design unseres Blogs.
Uns ist besonders wichtig, dass der Blog das Spannungsverhältnis Seriosität – Freude – Ruhe vermittelt.
Das Design soll folgendes transportieren:
• Seriös / glaubwürdig
• Hochwertig
• Sicherheit / Ruhe / Seelenfriede
• Hoffnung
• Positiv / herzlich / unbeschwert – aber dennoch ernsthaft
ZUM FARBKONZEPT ETC. SIEHE BITTE BRIEFING ANBEI

```html
<!DOCTYPE html>
<html lang="de">
<head>
<meta charset="utf-8">
<title>Wunschnest – Frauen Blog</title>
<link href="https://fonts.googleapis.com/css2?family=Noto+Serif:wght@400&family=Source+Sans+3:wght@400;600&display=swap" rel="stylesheet">
<style>
:root{
  --teal:#3fa9c2;
  --teal-dark:#2b8ea8;
  --teal-pale:#eaf5f8;
  --text:#3c3c3c;
  --muted:#a8a8a8;
  --line:#d9d9d9;
  --white:#ffffff;
}
*{box-sizing:border-box;margin:0;padding:0}
html,body{width:1200px;height:3659px;overflow:hidden;background:var(--white)}
body{position:relative;font-family:"Source Sans 3",sans-serif;color:var(--text)}
.abs{position:absolute}
.serif{font-family:"Noto Serif",serif}
.nav{position:absolute;top:12px;left:0;width:1200px;height:14px;font-size:10px;letter-spacing:.5px;color:#555}
.nav span{position:absolute;transform:translateX(-50%)}
.social{position:absolute;display:flex;gap:14px}
.social i{display:block;width:8px;height:8px;border-radius:50%;background:var(--teal)}
.search{position:absolute;left:1047px;top:10px;width:113px;height:18px;border-bottom:1px solid #eee;font-size:9px;color:#bbb;padding-left:6px;line-height:18px}
.logo{position:absolute;left:0;width:1200px;text-align:center;color:var(--teal);font-family:"Noto Serif",serif;font-size:48px;line-height:1}
.logo-sub{position:absolute;left:0;width:1200px;text-align:center;font-size:10px;letter-spacing:2px;color:#555}
.rule{position:absolute;height:1px;background:var(--line)}
.photo{position:absolute}
.cat{position:absolute;text-align:center;font-size:9px;letter-spacing:.5px;color:var(--teal)}
.cat b{font-weight:400;color:var(--teal);margin:0 18px}
.meta{position:absolute;text-align:center;font-size:8px;color:var(--muted)}
.more{position:absolute;text-align:center;font-size:9px;letter-spacing:.5px;color:var(--teal)}
.card-title{position:absolute;text-align:center;font-family:"Noto Serif",serif;font-size:15px;line-height:19px;color:var(--text)}
.post-title{position:absolute;left:161px;width:575px;text-align:center;font-family:"Noto Serif",serif;font-size:27px;line-height:37px;color:var(--text);font-weight:400}
.excerpt{position:absolute;left:161px;width:575px;font-size:14.6px;line-height:22.5px;text-align:justify;color:#555}
.drop{position:absolute;font-family:"Noto Serif",serif;font-size:68px;color:#bfe1ea;line-height:1}
.tagbar{position:absolute;left:161px;width:575px;height:31px;background:var(--teal-pale);font-size:8px;color:var(--muted);padding:0 14px;display:flex;align-items:center;justify-content:space-between}
.tagbar em{font-style:normal;color:var(--teal)}
.tagbar .ico{display:flex;gap:19px}
.tagbar .ico i{width:7px;height:7px;border-radius:50%;background:var(--teal);display:block}
.label{position:absolute;font-size:13px;letter-spacing:.4px;color:#333}
.rel-title{position:absolute;width:178px;text-align:center;font-family:"Noto Serif",serif;font-size:11.5px;line-height:17px;color:#444}
.sidebar-h{position:absolute;left:758px;width:278px;text-align:center;font-size:10px;letter-spacing:.4px;color:#333}
.welcome{position:absolute;left:758px;top:637px;width:278px;height:369px;border:1px solid #e5eef1}
.pop-title{position:absolute;left:867px;width:175px;font-family:"Noto Serif",serif;font-size:11px;line-height:17px;color:#333}
.pop-cat{position:absolute;left:867px;font-size:8.5px;color:var(--teal);letter-spacing:.4px}
.pop-meta{position:absolute;left:867px;font-size:7.5px;color:var(--muted)}
.cat-row{position:absolute;left:763px;width:272px;height:30px;border-bottom:1px solid #e4e4e4;font-family:"Noto Serif",serif;font-size:11px;color:var(--teal);display:flex;justify-content:space-between;align-items:center;padding:0 8px 0 0}
.cat-row span:first-child{border-left:1px solid var(--teal);padding-left:14px}
.cat-row span:last-child{color:#555;font-size:10px;font-family:"Source Sans 3",sans-serif}
.tag{position:absolute;height:21px;background:var(--teal-pale);font-size:7.5px;color:var(--teal);text-align:center;line-height:21px}
.footer{position:absolute;left:37px;top:3362px;width:1122px;height:239px;background:linear-gradient(180deg,#4fb6cc,#3ea5bf)}
.footer-nav{position:absolute;left:0;top:166px;width:1122px;height:35px;background:#2f8ea9;color:#fff;font-size:10px;letter-spacing:.5px}
.footer-nav span{position:absolute;top:11px;transform:translateX(-50%)}
</style>
</head>
<body>

<!-- header -->
<div class="social" style="left:39px;top:15px"><i></i><i></i><i></i><i></i></div>
<nav class="nav">
  <span style="left:324px">MODE</span><span style="left:403px">BEAUTY</span><span style="left:504px">SELBERMACHEN</span><span style="left:620px">WOHLFÜHLEN</span><span style="left:712px">LIEBE</span><span style="left:790px">FAMILIE</span><span style="left:870px">LEBEN</span>
</nav>
<div class="search">Search
  <svg class="abs" style="right:0;top:5px" width="9" height="9" viewBox="0 0 10 10"><circle cx="4" cy="4" r="3" fill="none" stroke="#3fa9c2" stroke-width="1.3"/><line x1="6.3" y1="6.3" x2="9" y2="9" stroke="#3fa9c2" stroke-width="1.3"/></svg>
</div>
<div class="logo" style="top:60px">Wunschnest</div>
<div class="logo-sub" style="top:115px">FRAUEN BLOG</div>
<div class="rule" style="left:37px;top:156px;width:1125px"></div>

<!-- featured -->
<div class="photo" role="img" aria-label="Kleines Mädchen mit gestrickter Mütze" style="left:161px;top:185px;width:276px;height:276px;background:linear-gradient(160deg,#c9a35a,#d98b6a 55%,#f0d8c8)"></div>
<div class="photo" role="img" aria-label="Schwangere Frau in weißem Raum mit Kerzen" style="left:460px;top:185px;width:276px;height:276px;background:linear-gradient(160deg,#e9e9e9,#d8d4d0 60%,#c9c1b8)"></div>
<div class="photo" role="img" aria-label="Baby mit Stirnband im bedruckten Body" style="left:758px;top:185px;width:276px;height:276px;background:linear-gradient(160deg,#c7c3cd,#b49aac 60%,#e7e3e6)"></div>
<div class="cat" style="left:161px;width:276px;top:205px;color:#fff">GESUNDHEIT</div>
<div class="cat" style="left:460px;width:276px;top:205px;color:#fff">BEAUTY</div>
<div class="cat" style="left:758px;width:276px;top:205px;color:#fff">MODE</div>
<div class="meta" style="left:161px;width:276px;top:477px">May 25, 2017</div>
<div class="meta" style="left:460px;width:276px;top:477px">May 25, 2017</div>
<div class="meta" style="left:758px;width:276px;top:477px">May 25, 2017</div>
<div class="card-title" style="left:171px;width:256px;top:494px">Lorem ipsum dolor sit amet, consectetur adipiscing elit</div>
<div class="card-title" style="left:470px;width:256px;top:494px">Mauris convallis pulvinar nulla, vel bibendum enim</div>
<div class="card-title" style="left:768px;width:256px;top:494px">6 Stylish Summer Kinder Color Palettes</div>
<div class="more" style="left:161px;width:276px;top:547px">READ MORE</div>
<div class="more" style="left:460px;width:276px;top:547px">READ MORE</div>
<div class="more" style="left:758px;width:276px;top:547px">READ MORE</div>
<div class="rule" style="left:37px;top:587px;width:1125px"></div>

<!-- post 1 -->
<div class="cat" style="left:161px;width:575px;top:636px"><b>|</b>SCHWANGERSCHAFT<b>|</b></div>
<div class="meta" style="left:161px;width:575px;top:661px">May 25, 2017 &nbsp;·&nbsp; 4 comments</div>
<h1 class="post-title" style="top:684px">Verbote während der Schwangerschaft: Das sollten Sie besser nicht tun</h1>
<div class="photo" role="img" aria-label="Schwangere Frau im blauen Kleid im warmen Abendlicht" style="left:161px;top:797px;width:575px;height:359px;background:linear-gradient(120deg,#f3d3a0,#d9a66a 45%,#8d8aa0 75%,#c48c58)"></div>
<div class="drop" style="left:157px;top:1163px">W</div>
<p class="excerpt" style="top:1178px;padding-left:18px">Wer während der Schwangerschaft krank wird muss aufpassen, welche Medikamente er zu sich nimmt. Viele sind während der Schwangerschaft nicht erlaubt oder müssen in Absprache mit dem Arzt eingenommen werden. Auch bei rezeptfreien Medikamenten sollten Sie Rücksprache mit Ihrem Arzt, der Hebamme</p>
<div class="more" style="left:161px;width:575px;top:1290px">READ MORE</div>
<div class="tagbar" style="top:1332px"><span>TAGS: &nbsp;<em>GESUND; SCHWANGERSCHAFT</em></span><span class="ico"><i></i><i></i><i></i><i></i></span></div>
<div class="label" style="left:160px;top:1393px">RELATED POSTS</div>
<div class="photo" role="img" aria-label="Familie mit Tochter im Park" style="left:160px;top:1432px;width:178px;height:177px;background:linear-gradient(160deg,#7fa24e,#b5c58b 55%,#e8e4d6)"></div>
<div class="photo" role="img" aria-label="Frau mit Baby in Tragetuch am See" style="left:361px;top:1432px;width:177px;height:177px;background:linear-gradient(160deg,#8e9aa5,#c9a9b3 55%,#6f7f8d)"></div>
<div class="photo" role="img" aria-label="Schwangere Frau mit Blumenkranz" style="left:560px;top:1432px;width:177px;height:177px;background:linear-gradient(160deg,#ececec,#dccfd0 60%,#c9bcb7)"></div>
<div class="cat" style="left:160px;width:178px;top:1621px"><b>|</b>FAMILIE<b>|</b></div>
<div class="cat" style="left:361px;width:177px;top:1621px"><b>|</b>SELBERMACHEN<b>|</b></div>
<div class="cat" style="left:560px;width:177px;top:1621px"><b>|</b>BEAUTY<b>|</b></div>
<div class="rel-title" style="left:160px;top:1640px">Maecenas libero leo, egestas eu lobortis ut, egestas consequat</div>
<div class="rel-title" style="left:360px;top:1640px">Nam vitae dignissim quam</div>
<div class="rel-title" style="left:559px;top:1640px">Aliquam elementum, sapien ac consectetur ultricies</div>
<div class="meta" style="left:160px;width:178px;top:1684px">May 25, 2017 &nbsp;·&nbsp; 4 comments</div>
<div class="meta" style="left:361px;width:177px;top:1684px">May 25, 2017 &nbsp;·&nbsp; 4 comments</div>
<div class="meta" style="left:560px;width:177px;top:1684px">May 25, 2017 &nbsp;·&nbsp; 4 comments</div>
<div class="rule" style="left:160px;top:1723px;width:577px;background:#e6e6e6"></div>

<!-- post 2 -->
<div class="cat" style="left:161px;width:575px;top:1774px"><b>|</b>MODE<b>|</b></div>
<div class="meta" style="left:161px;width:575px;top:1800px">May 25, 2017 &nbsp;·&nbsp; 4 comments</div>
<h2 class="post-title" style="top:1822px">Mauris venenatis mattis orci, et tristique orci dapibus vitae</h2>
<div class="photo" role="img" aria-label="Schwangere Frau im lila Kimono auf einer sonnigen Wiese" style="left:161px;top:1934px;width:575px;height:808px;background:linear-gradient(180deg,#d9ddc4,#b8b48e 35%,#9aa866 65%,#a9b86a)"></div>
<div class="drop" style="left:153px;top:2762px">A</div>
<p class="excerpt" style="top:2777px;padding-left:13px">Aenean tristique sit amet metus vitae commodo. Quisque congue finibus vehicula. Integer tincidunt aliquet leo. Fusce eget ullamcorper orci. Phasellus pellentesque ut dui ac consequat. Vestibulum quis orci non velit varius ullamcorper ut sit amet tellus. Lorem ipsum dolor sit amet, consectetur adipiscing elit. Quisque urna urna, ultrices vitae</p>
<div class="more" style="left:161px;width:575px;top:2891px">READ MORE</div>
<div class="tagbar" style="top:2936px"><span>TAGS: &nbsp;<em>GESUND; SCHWANGERSCHAFT</em></span><span class="ico"><i></i><i></i><i></i><i></i></span></div>
<div class="label" style="left:160px;top:3006px">RELATED POSTS</div>
<div class="photo" role="img" aria-label="Familie mit Tochter im Park" style="left:160px;top:3045px;width:178px;height:177px;background:linear-gradient(160deg,#7fa24e,#b5c58b 55%,#e8e4d6)"></div>
<div class="photo" role="img" aria-label="Frau mit Baby in Tragetuch am See" style="left:361px;top:3045px;width:177px;height:177px;background:linear-gradient(160deg,#8e9aa5,#c9a9b3 55%,#6f7f8d)"></div>
<div class="photo" role="img" aria-label="Schwangere Frau mit Blumenkranz" style="left:560px;top:3045px;width:177px;height:177px;background:linear-gradient(160deg,#ececec,#dccfd0 60%,#c9bcb7)"></div>
<div class="cat" style="left:160px;width:178px;top:3234px"><b>|</b>FAMILIE<b>|</b></div>
<div class="cat" style="left:361px;width:177px;top:3234px"><b>|</b>SELBERMACHEN<b>|</b></div>
<div class="cat" style="left:560px;width:177px;top:3234px"><b>|</b>BEAUTY<b>|</b></div>
<div class="rel-title" style="left:160px;top:3253px">Maecenas libero leo, egestas eu lobortis ut, egestas consequat</div>
<div class="rel-title" style="left:360px;top:3253px">Nam vitae dignissim quam</div>
<div class="rel-title" style="left:559px;top:3253px">Aliquam elementum, sapien ac consectetur ultricies</div>
<div class="meta" style="left:160px;width:178px;top:3297px">May 25, 2017 &nbsp;·&nbsp; 4 comments</div>
<div class="meta" style="left:361px;width:177px;top:3297px">May 25, 2017 &nbsp;·&nbsp; 4 comments</div>
<div class="meta" style="left:560px;width:177px;top:3297px">May 25, 2017 &nbsp;·&nbsp; 4 comments</div>
<div class="rule" style="left:160px;top:3337px;width:577px;background:#e6e6e6"></div>

<!-- sidebar: welcome -->
<aside class="welcome">
  <div class="abs" role="img" aria-label="Türkis-weißes Zickzackmuster" style="left:-1px;top:-1px;width:278px;height:141px;background:linear-gradient(180deg,#7fcbd9,#a9dbe4)"></div>
  <div class="abs" role="img" aria-label="Porträt der Bloggerin" style="left:60px;top:35px;width:156px;height:156px;border-radius:50%;border:5px solid #fff;background:linear-gradient(160deg,#e5c3a6,#b98a62)"></div>
  <div class="abs serif" style="left:0;width:276px;top:212px;text-align:center;color:var(--teal);font-size:15px">Welcome!</div>
  <p class="abs" style="left:12px;width:252px;top:244px;text-align:center;font-size:13.5px;line-height:22px;color:#555">Get inspired by talent from around the world. It's a real source of inspiration and style for millions people.</p>
  <div class="abs" style="left:0;width:276px;top:329px;text-align:center;font-size:9px;color:var(--teal);letter-spacing:.5px">ABOUT ME</div>
</aside>

<!-- sidebar: popular -->
<div class="sidebar-h" style="top:1035px">MOST POPULAR ARTICLES</div>
<div class="photo" role="img" aria-label="Brautstrauß mit Kupferdeko" style="left:758px;top:1068px;width:91px;height:89px;background:linear-gradient(160deg,#8c9b7a,#5d6650 55%,#c9b8a6)"></div>
<div class="photo" role="img" aria-label="Mädchen mit Blumenkranz" style="left:758px;top:1180px;width:91px;height:89px;background:linear-gradient(160deg,#c9d7b0,#e5cfc9 55%,#a5b77f)"></div>
<div class="photo" role="img" aria-label="Geschenke mit Blumen" style="left:758px;top:1290px;width:91px;height:90px;background:linear-gradient(160deg,#e3b7b9,#d8c6ad 55%,#b49b84)"></div>
<div class="pop-cat" style="top:1072px">|&nbsp;&nbsp;&nbsp;&nbsp; DEKORATION &nbsp;&nbsp;&nbsp;&nbsp;|</div>
<div class="pop-title" style="top:1095px">Dreamy Point Reyes Elopement Inspiration with Copper</div>
<div class="pop-meta" style="top:1138px">May 25, 2017 &nbsp;·&nbsp; 4 comments</div>
<div class="pop-cat" style="top:1184px">|&nbsp;&nbsp;&nbsp;&nbsp; MODE &nbsp;&nbsp;&nbsp;&nbsp;|</div>
<div class="pop-title" style="top:1207px">6 Ideas for an Eco-Friendly Wedding</div>
<div class="pop-meta" style="top:1250px">May 25, 2017 &nbsp;·&nbsp; 4 comments</div>
<div class="pop-cat" style="top:1295px">|&nbsp;&nbsp;&nbsp;&nbsp; DEKORATION &nbsp;&nbsp;&nbsp;&nbsp;|</div>
<div class="pop-title" style="top:1318px">Gift Ideas for Everyone On Your List</div>
<div class="pop-meta" style="top:1361px">May 25, 2017 &nbsp;·&nbsp; 4 comments</div>

<!-- sidebar: categories -->
<div class="sidebar-h" style="top:1413px">CATEGORY</div>
<div class="cat-row" style="top:1434px"><span>MODE</span><span>(52)</span></div>
<div class="cat-row" style="top:1464px"><span>BEAUTY</span><span>(12)</span></div>
<div class="cat-row" style="top:1494px"><span>SELBERMACHEN</span><span>(7)</span></div>
<div class="cat-row" style="top:1524px"><span>LIEBE</span><span>(11)</span></div>
<div class="cat-row" style="top:1554px"><span>FAMILIE</span><span>(4)</span></div>

<!-- sidebar: tags -->
<div class="sidebar-h" style="top:1617px">TAGS</div>
<div class="tag" style="left:759px;top:1648px;width:48px">MODE</div>
<div class="tag" style="left:811px;top:1648px;width:66px">CEREMONY</div>
<div class="tag" style="left:881px;top:1648px;width:98px">SELBERMACHEN</div>
<div class="tag" style="left:983px;top:1648px;width:52px">LIEBE</div>
<div class="tag" style="left:759px;top:1678px;width:82px">DECORATIONS</div>
<div class="tag" style="left:845px;top:1678px;width:50px">FOOD</div>
<div class="tag" style="left:899px;top:1678px;width:62px">FAMILIE</div>

<!-- sidebar: newsletter -->
<div class="photo" role="img" aria-label="Blumen auf hellblauem Holzuntergrund" style="left:758px;top:1735px;width:278px;height:204px;background:linear-gradient(160deg,#cfe4ea,#d9e8ec 50%,#e2d4e2)"></div>
<div class="abs" style="left:758px;width:278px;top:1772px;text-align:center;font-size:13px;line-height:18px;color:#444;letter-spacing:.3px">SUBSCRIBE<br>TO NEWSLETTER</div>
<div class="abs" style="left:792px;top:1829px;width:212px;height:30px;background:#fff;font-size:7.5px;color:#bbb;text-align:center;line-height:30px">Enter your email address</div>
<div class="abs" style="left:792px;top:1869px;width:212px;height:31px;background:#47adc7;color:#fff;font-size:10px;letter-spacing:.5px;text-align:center;line-height:31px;font-weight:600">SEND</div>

<!-- sidebar: social page box -->
<div class="abs" style="left:758px;top:1985px;width:278px;height:177px;border:1px solid #e4e4e4"></div>
<div class="photo" role="img" aria-label="Hellblaues florales Titelbild" style="left:759px;top:1986px;width:276px;height:106px;background:linear-gradient(160deg,#bfe3ea,#a6d6e0)"></div>
<div class="abs" style="left:765px;top:1994px;width:48px;height:48px;background:#f3f8fa;border:2px solid #fff"></div>
<div class="abs serif" style="left:823px;top:1996px;font-size:13px;color:#fff">Wunschnest</div>
<div class="abs" style="left:771px;top:2060px;width:78px;height:20px;background:#fff;font-size:10px;color:#333;line-height:20px;padding-left:6px;display:flex;align-items:center;gap:4px"><i style="width:9px;height:9px;background:#4a69ad;display:block"></i>Like Page</div>
<div class="abs" style="left:969px;top:2060px;width:57px;height:20px;background:#fff;font-size:10px;color:#333;line-height:20px;text-align:center">➦ Share</div>
<div class="abs" style="left:767px;top:2100px;width:262px;height:52px;border:1px solid #e4e4e4;background:#fff"></div>
<div class="abs" style="left:775px;top:2104px;font-size:10px;color:#333">Be the first of your friends to like this</div>
<div class="abs" role="img" aria-label="Profilbilder von Freunden" style="left:775px;top:2121px;width:218px;height:26px;background:linear-gradient(90deg,#3d5066,#9b8060,#5a6f4d,#b45c4c,#4e6e8a,#8a7160)"></div>

<!-- footer -->
<footer class="footer" role="img" aria-label="Türkisfarbenes Zickzackmuster">
  <div class="logo" style="left:0;width:1122px;top:55px;color:#fff">Wunschnest</div>
  <div class="logo-sub" style="left:0;width:1122px;top:110px;color:#2d6d80">FRAUEN BLOG</div>
  <div class="abs" style="left:985px;top:140px;width:40px;height:40px;background:#5cc0d4;color:#fff;font-size:8px;text-align:center;padding-top:21px">
    <svg class="abs" style="left:14px;top:8px" width="12" height="7" viewBox="0 0 12 7"><path d="M1 6 L6 1 L11 6" fill="none" stroke="#fff" stroke-width="1.2"/></svg>TOP</div>
  <nav class="footer-nav">
    <span style="left:287px">MODE</span><span style="left:366px">BEAUTY</span><span style="left:467px">SELBERMACHEN</span><span style="left:583px">WOHLFÜHLEN</span><span style="left:675px">LIEBE</span><span style="left:753px">FAMILIE</span><span style="left:833px">LEBEN</span>
  </nav>
</footer>
<div class="abs" style="left:0;width:1200px;top:3617px;text-align:center;font-size:8px;color:var(--muted)">Copyrights 2017 All Rights Reserved.</div>

</body>
</html>
```